Quiet Verses Across Winter Evenings

Need a BOOK COVER, SPINE, and BACK for above named book. This is the story of my late wife (a university professor) told through her own songs and poems. It is about the people she loved, especially her grand children, her extensive professional and life interests, her family, friends, and festivities, her illness, etc.
Updates

Need extra days to review

Target Market(s)

Family and friends

Font styles to use
Other font styles liked:
• Times New Roman

Requirements
Must have
• Regret I haven't given much thought to it...
Nice to have
• Regret I haven't given much thought to it..
Should not have

```html
<!DOCTYPE html>
<html lang="en">
<head>
<meta charset="utf-8">
<title>Quiet Verses Across Winter Evenings – Book Jacket</title>
<link href="https://fonts.googleapis.com/css2?family=Comfortaa:wght@300;400&family=Barlow:wght@400&display=swap" rel="stylesheet">
<style>
  :root {
    --paper: #ffffff;
    --night: #050507;
    --lavender: #8e93d6;
    --lavender-pale: #b4afd4;
    --ink: #111114;
    --snow: #f2f2f4;
  }
  * { margin: 0; padding: 0; box-sizing: border-box; }
  html, body { width: 1200px; height: 1000px; overflow: hidden; background: var(--paper); }
  .jacket { position: relative; width: 1200px; height: 1000px; }

  .back-cover {
    position: absolute; left: 10px; top: 75px; width: 566px; height: 850px; overflow: hidden;
    background:
      radial-gradient(ellipse 60% 52% at 50% 66%, var(--lavender-pale) 0%, #a7a2c6 45%, rgba(120,115,150,0.6) 72%, rgba(5,5,7,0) 100%),
      linear-gradient(172deg, rgba(5,5,7,0) 16%, rgba(200,210,215,0.45) 25%, rgba(90,110,120,0.2) 33%, rgba(5,5,7,0) 42%),
      var(--night);
  }
  .back-title { position: absolute; left: 66px; top: 62px; font-family: "Comfortaa", sans-serif; font-weight: 300; }
  .back-title .main { display: block; color: var(--lavender); font-size: 30px; letter-spacing: 0.3px; }
  .back-title .sub { display: block; color: var(--snow); font-size: 19px; font-weight: 400; margin-top: 2px; }
  .blurb {
    position: absolute; left: 63px; top: 236px; width: 440px;
    font-family: "Barlow", sans-serif; font-size: 13.6px; line-height: 19px;
    color: var(--ink); text-align: center;
  }
  .blurb p { margin-bottom: 19px; }
  .blurb p.last { margin-top: 39px; }

  .spine {
    position: absolute; left: 576px; top: 75px; width: 46px; height: 850px;
    background: var(--night);
  }
  .spine-title, .spine-author {
    position: absolute; left: 11px;
    writing-mode: vertical-rl; font-family: "Comfortaa", sans-serif; font-size: 17px;
    white-space: nowrap; color: var(--snow);
  }
  .spine-title { top: 68px; }
  .spine-title .accent { color: var(--lavender); }
  .spine-author { top: 500px; }

  .front-cover {
    position: absolute; left: 622px; top: 75px; width: 568px; height: 850px; overflow: hidden;
    background:
      radial-gradient(ellipse 60% 30% at 55% 90%, rgba(74,106,168,0.55), rgba(5,5,7,0) 75%),
      linear-gradient(174deg, rgba(5,5,7,0) 10%, rgba(190,200,205,0.5) 20%, rgba(120,135,140,0.25) 28%, rgba(210,215,220,0.45) 36%, rgba(5,5,7,0) 48%),
      var(--night);
  }
  .artwork {
    position: absolute; left: 50px; top: 190px; width: 470px; height: 560px;
    background: radial-gradient(ellipse 50% 48% at 50% 55%, #e9eef0 0%, #b9ccd0 35%, rgba(60,111,120,0.55) 62%, rgba(5,5,7,0) 85%);
  }
  .front-heading { position: absolute; inset: 0; font-weight: 300; }
  .title-line {
    position: absolute; font-family: "Comfortaa", sans-serif; color: var(--lavender); font-weight: 300;
  }
  .title-quiet { left: 42px; top: 24px; font-size: 74px; }
  .title-verses { left: 250px; top: 108px; font-size: 62px; }
  .subtitle-line {
    position: absolute; font-family: "Comfortaa", sans-serif; color: var(--snow); font-weight: 300;
  }
  .subtitle-across { left: 76px; top: 226px; font-size: 34px; }
  .subtitle-evenings { left: 76px; top: 272px; font-size: 36px; }
  .front-author {
    position: absolute; left: 0; width: 100%; top: 770px; text-align: center;
    font-family: "Comfortaa", sans-serif; color: var(--snow); font-size: 29px; letter-spacing: 0.5px;
  }
</style>
</head>
<body>
<div class="jacket">

  <section class="back-cover">
    <h2 class="back-title">
      <span class="main">Quiet Verses</span>
      <span class="sub">Across Winter Evenings</span>
    </h2>
    <div class="blurb">
      <p>Lorem ipsum dolor sit amet, consectetur adipiscing elit, sed do eiusmod tempor incididunt ut labore et dolore magna aliqua. Quis ipsum suspendisse ultrices gravida. Risus commodo viverra maecenas accumsan lacus vel facilisis.</p>
      <p>Lorem ipsum dolor sit amet, consectetur adipiscing elit, sed do eiusmod tempor incididunt ut labore et dolore magna aliqua. Quis ipsum suspendisse ultrices gravida. Risus commodo viverra maecenas accumsan lacus vel facilisis.</p>
      <p>Lorem ipsum dolor sit amet, consectetur adipiscing elit, sed do eiusmod tempor incididunt ut labore et dolore magna aliqua. Quis ipsum suspendisse ultrices gravida. Risus commodo viverra maecenas accumsan lacus vel facilisis.</p>
      <p>Lorem ipsum dolor sit amet, consectetur adipiscing elit, sed do eiusmod tempor incididunt ut labore et dolore magna aliqua. Quis ipsum suspendisse ultrices gravida. Risus commodo viverra maecenas accumsan lacus vel facilisis.</p>
      <p class="last">Lorem ipsum dolor sit amet, consectetur adipiscing elit, sed do eiusmod tempor incididunt ut labore et dolore magna aliqua. Quis ipsum suspendisse ultrices gravida.</p>
    </div>
  </section>

  <section class="spine">
    <div class="spine-title"><span class="accent">Quiet Verses</span>&nbsp;Across Winter Evenings</div>
    <div class="spine-author">Leela Varadkar Mehta</div>
  </section>

  <section class="front-cover">
    <div class="artwork" role="img" aria-label="Illustration of cupped hands holding a bird's nest with blue eggs, surrounded by purple and green flowers and leafy sprigs over a glowing cracked-ice backdrop"></div>
    <h1 class="front-heading">
      <span class="title-line title-quiet">Quiet</span>
      <span class="title-line title-verses">Verses</span>
      <span class="subtitle-line subtitle-across">Across</span>
      <span class="subtitle-line subtitle-evenings">Winter Evenings</span>
    </h1>
    <div class="front-author">Leela Varadkar Mehta</div>
  </section>

</div>
</body>
</html>
```